New Business Card Design for Manufacturing

We are an engineering/manufacturing company that offers Advanced machining/assembly/engineering services, as well as innovative products for the heavy duty engine cooling markets.

We are looking to get a new business card designed that is clean and modern looking, but still fits the wide range of technical/skilled work we do.

- We hope to use this design as the base for other design work in new Presentations, web, and print work.

Industry/Entity Type

Engineering

Contact Information for Business Card

Our preferred color of blue is (RGB) 22/71/159 but can vary slightly from that color. Our content will be our Logo and full company name (Fabricated Tooling Works, Inc.), company address, name, job title, phone number with extension, cell number, fax number, website, and email address on the cards.
We'd like the full company name next to the logo, but we are open to other interpretations of that layout.
Preferably, we would like the back side to be clean with just our logo, and the front to contain all of the contact information.

Colors
2f74b4
0355a3
85abd2

Requirements
Must have
• - Logo, company name, needed content - We are open to interpretation beyond that.
• - Standard size business card.
• - Horizontal orientation.
• - Enough space for lengthy names / job titles (for example, a job title could read "Directory of Human Resources" or "V.P. of Governmental Affairs"). We need this to look clean, whether the title be short (CEO) or long (as described above).

```html
<!DOCTYPE html>
<html lang="en">
<head>
<meta charset="utf-8">
<title>Fabricated Tooling Works – Business Card</title>
<link rel="stylesheet" href="https://fonts.googleapis.com/css2?family=Montserrat:wght@400;500;600;700;800;900&display=swap">
<style>
  :root {
    --page: #2b2b2d;
    --card: #050505;
    --blue: #16479f;
    --blue-bright: #1f5fc4;
    --white: #ffffff;
    --grey: #8a8d93;
    --pattern: #151618;
  }
  * { box-sizing: border-box; margin: 0; padding: 0; }
  html, body { width: 1200px; height: 900px; overflow: hidden; }
  body {
    background: var(--page);
    font-family: "Montserrat", Arial, sans-serif;
    display: flex; flex-direction: column; align-items: center; justify-content: center;
    gap: 40px;
  }
  .card {
    position: relative; width: 630px; height: 360px;
    background: var(--card); overflow: hidden;
    box-shadow: 0 14px 30px rgba(0,0,0,.45);
  }
  .card svg.bands { position: absolute; inset: 0; width: 100%; height: 100%; }

  /* back side */
  .back .pattern {
    position: absolute; inset: 0;
    background: radial-gradient(circle at 86% 32%, #1b1f27 0, #0d0e11 38%, transparent 60%),
                linear-gradient(120deg, var(--pattern), #0a0a0b 70%);
  }
  .back .lockup {
    position: absolute; left: 34px; top: 152px;
    display: flex; align-items: flex-end; gap: 18px;
  }
  .back .mark-block { display: flex; flex-direction: column; }
  .back .mark { font-size: 78px; font-weight: 900; color: var(--white); line-height: .9; letter-spacing: 2px; }
  .back .tagline { font-size: 14px; font-weight: 700; color: var(--grey); letter-spacing: .5px; margin-top: 6px; }
  .back .company {
    font-size: 16px; font-weight: 800; color: var(--white); line-height: 1.05;
    text-transform: uppercase; margin-bottom: 26px;
  }
  .back .company small { font-size: 8px; font-weight: 700; margin-left: 3px; }

  /* front side */
  .front .mark-block { position: absolute; left: 34px; top: 30px; display: flex; flex-direction: column; }
  .front .mark { font-size: 84px; font-weight: 900; color: var(--blue-bright); line-height: .9; letter-spacing: 2px; }
  .front .tagline { font-size: 15px; font-weight: 700; color: var(--grey); letter-spacing: .5px; margin-top: 6px; }
  .contact { position: absolute; left: 38px; top: 196px; list-style: none; }
  .contact li { display: flex; align-items: center; gap: 10px; color: var(--white); font-size: 15px; line-height: 21px; }
  .contact svg { width: 15px; height: 15px; flex: none; }
  .contact .address { margin-top: 4px; }
  .person { position: absolute; right: 34px; top: 206px; text-align: right; }
  .person .name { font-size: 19px; font-weight: 700; color: var(--blue-bright); text-transform: uppercase; line-height: 24px; }
  .person .title { font-size: 14px; color: var(--white); margin-top: 2px; line-height: 18px; }
  .website { position: absolute; right: 40px; top: 300px; color: var(--white); font-size: 15px; line-height: 20px; letter-spacing: 1px; }
</style>
</head>
<body>

<section class="card back" aria-label="Card back">
  <div class="pattern" role="img" aria-label="Faint pattern of machining icons and a network globe"></div>
  <svg class="bands" viewBox="0 0 630 360" aria-hidden="true">
    <polygon points="0,290 300,290 332,322 0,322" fill="var(--blue)"/>
    <polyline points="0,328 340,328 380,268 630,268" fill="none" stroke="var(--white)" stroke-width="6"/>
  </svg>
  <div class="lockup">
    <div class="mark-block">
      <span class="mark">FTW</span>
      <span class="tagline">BUILT TO LAST</span>
    </div>
    <p class="company">Fabricated<br>Tooling<br>Works<small>INC</small></p>
  </div>
</section>

<section class="card front" aria-label="Card front">
  <svg class="bands" viewBox="0 0 630 360" aria-hidden="true">
    <polygon points="426,288 630,288 630,332 410,332" fill="var(--blue)"/>
    <polyline points="0,342 400,342 420,282 630,282" fill="none" stroke="var(--white)" stroke-width="6"/>
  </svg>
  <div class="mark-block">
    <span class="mark">FTW</span>
    <span class="tagline">BUILT TO LAST</span>
  </div>
  <ul class="contact">
    <li><svg viewBox="0 0 16 16"><circle cx="8" cy="8" r="7" fill="none" stroke="#1f5fc4" stroke-width="1.5"/><path d="M5.5 4.5l1.5 1.5-1 1c.5 1.2 1.3 2 2.5 2.5l1-1 1.5 1.5-1 1.2C7.5 11 5 8.5 4.5 6z" fill="#1f5fc4"/></svg>(502) 555-0148 x210</li>
    <li><svg viewBox="0 0 16 16"><circle cx="8" cy="8" r="7" fill="none" stroke="#1f5fc4" stroke-width="1.5"/><rect x="6" y="4" width="4" height="8" rx="1" fill="none" stroke="#1f5fc4" stroke-width="1.2"/></svg>502-555-0193</li>
    <li><svg viewBox="0 0 16 16"><circle cx="8" cy="8" r="7" fill="none" stroke="#1f5fc4" stroke-width="1.5"/><rect x="5" y="6" width="6" height="5" fill="#1f5fc4"/><rect x="6" y="4" width="4" height="2" fill="#1f5fc4"/></svg>502-555-0177</li>
    <li><svg viewBox="0 0 16 16"><circle cx="8" cy="8" r="7" fill="none" stroke="#1f5fc4" stroke-width="1.5"/><rect x="4.5" y="5.5" width="7" height="5" fill="none" stroke="#1f5fc4" stroke-width="1.2"/><path d="M4.5 5.5l3.5 3 3.5-3" fill="none" stroke="#1f5fc4" stroke-width="1.2"/></svg>mark@ftworks.org</li>
    <li class="address">418 Larch Rd, Bardwell KY 42023</li>
  </ul>
  <div class="person">
    <p class="name">Mark Ellison</p>
    <p class="title">V.P. of Governmental Affairs</p>
  </div>
  <p class="website">www.ftworks.com</p>
</section>

</body>
</html>
```